FOOD SUPPLEMENT FOR SOAR THROAT - TELVAROSE

I need a design for a food supplement product. The product is a formulation designed to combat bacteria that causes infections in the throat. Due to the fact that is a food supplment the design has to be away from the regular farmacy products. The design has to be elegant in the same time to shows the seriousness of the product. Need to have 3 pictograms for gluten , sugar and lactose free, the photo of the ingredients is an option. As colors yellow, orange, lime green and dark blue is preferable. In attached the dimensions of the box, the logo of the name of the product and the old box where the 3 pictograms Ithe ingredients are Murraya paniculata, Vitamin C, Malva sylvestris and Filipendula ulmaria. The title under the name is Food supplement in functional chewing gum and in italian Integratore alimentare in chewing gum funzionale.

Industry/Entity Type

pharmaceutical

Colors
0054AA
0677BA
7BADD7
CADEEF
E8F1F8
59FF00
82FF00
B8FF75
E3FFCB
F4FFEA
FFF300
FFF600
FEFA6F
FFFEC7
FFFEE8
F0912C
F2A743
F7CA91
FBE8D2
FDF5EE

Requirements
Must have
• pictograms -gluten, lactose, sugar free

```html
<!DOCTYPE html>
<html lang="en">
<head>
<meta charset="utf-8">
<title>FUSTELLA chol control – TELVAROSE</title>
<link href="https://fonts.googleapis.com/css2?family=Open+Sans:wght@400;700;800&family=Montserrat:wght@400;600;700&family=Parisienne&display=swap" rel="stylesheet">
<style>
:root{
  --paper:#ffffff;
  --ink:#231f20;
  --box-blue:#214f96;
  --box-edge:#2f62b0;
  --front-light:#2f93da;
  --front-mid:#2a6fc0;
  --front-dark:#233f8a;
  --badge-navy:#223e86;
  --lime:#d6e32a;
  --lime-dark:#b7c61c;
  --leaf-green:#1f9c0c;
  --orange:#f0751c;
  --gum-purple:#8c3fa0;
  --varnish:#fff200;
  --white:#ffffff;
}
*{margin:0;padding:0;box-sizing:border-box}
html,body{width:848px;height:1200px;overflow:hidden;background:var(--paper)}
.sheet{position:relative;width:848px;height:1200px;font-family:"Montserrat",sans-serif}
.sheet-title{position:absolute;left:45px;top:28px;font-family:"Open Sans",sans-serif;font-weight:700;font-size:42px;letter-spacing:-0.5px;color:var(--ink)}
.dieline{position:absolute;left:0;top:0}
.front{position:absolute;left:173px;width:495px;height:306px;color:var(--white);overflow:hidden;
  background:linear-gradient(160deg,var(--front-light) 0%,var(--front-mid) 45%,var(--front-dark) 100%)}
.front-1{top:237px}
.front-2{top:646px}
.front-glow{position:absolute;inset:0;
  background:radial-gradient(circle at 70% 34%,rgba(255,255,255,.75) 0,rgba(255,255,255,.18) 8%,rgba(255,255,255,0) 30%),
             radial-gradient(circle at 100% 90%,rgba(255,255,255,.35) 0,rgba(255,255,255,0) 12%)}
.count-badge{position:absolute;left:16px;top:9px;width:55px;height:55px;border-radius:50%;background:var(--badge-navy);text-align:center}
.count-badge .num{display:block;font-family:"Open Sans",sans-serif;font-weight:700;font-size:30px;line-height:32px;margin-top:6px}
.count-badge .unit{display:block;font-family:"Open Sans",sans-serif;font-size:8px;line-height:8px}
.fast-badge{position:absolute;left:29px;top:141px;width:56px;height:56px;border-radius:50%;background:var(--lime);border:1.5px solid var(--lime-dark);box-shadow:inset 0 0 0 2px var(--lime),inset 0 0 0 3px var(--lime-dark);text-align:center}
.fast-badge .fast{display:block;font-family:"Open Sans",sans-serif;font-weight:700;font-size:19px;line-height:19px;color:var(--orange);margin-top:12px}
.fast-badge .acting{display:block;font-family:"Montserrat",sans-serif;font-size:8px;color:var(--leaf-green);margin-left:10px}
.brand-name{position:absolute;font-family:"Open Sans",sans-serif;font-weight:800;color:var(--lime);letter-spacing:-1px;line-height:1;white-space:nowrap}
.front .brand-name{left:163px;top:88px;font-size:48px}
.supplement-tag{position:absolute;background:var(--leaf-green);color:var(--white);font-family:"Open Sans",sans-serif;text-align:center;white-space:nowrap}
.front .supplement-tag{left:147px;top:139px;width:163px;height:25px;font-size:17px;line-height:25px}
.claim{position:absolute;font-family:"Parisienne",cursive;color:var(--white);white-space:nowrap;line-height:1.2}
.front .claim{left:240px;top:162px;font-size:29px}
.benefits{position:absolute;left:14px;top:243px;list-style:none;font-size:10.5px;line-height:15.5px}
.free-icons{position:absolute;left:258px;top:242px;display:flex;gap:8px}
.free-icon{width:46px;text-align:center;font-size:8.5px;line-height:9px}
.free-icon svg{display:block;margin:0 auto 3px}
.free-icon b{font-weight:700}
.side-strip{position:absolute;left:173px;width:495px;height:103px;color:var(--white)}
.strip-1{top:543px}
.strip-2{top:951px}
.side-strip .supplement-tag{left:17px;top:35px;width:200px;height:25px;font-size:20px;line-height:25px}
.side-strip .claim{left:80px;top:58px;font-size:28px}
.side-strip .brand-name{left:318px;top:50px;font-size:26px}
.side-panel{position:absolute;left:668px;top:237px;width:91px;height:306px}
.varnish-area{position:absolute;left:12px;top:139px;width:44px;height:86px;background:var(--varnish);display:flex;align-items:center;justify-content:center}
.varnish-area span{transform:rotate(-90deg);white-space:nowrap;font-family:"Open Sans",sans-serif;font-size:7px;color:var(--ink);letter-spacing:-.3px}
.batch-info{position:absolute;left:18px;top:240px;width:54px;height:56px;display:flex;align-items:center;justify-content:center}
.batch-info p{transform:rotate(-90deg);white-space:nowrap;font-size:6px;line-height:7.5px;color:#0e2450}
</style>
</head>
<body>
<div class="sheet">
  <h1 class="sheet-title">FUSTELLA chol control</h1>

  <svg class="dieline" width="848" height="1200" viewBox="0 0 848 1200" aria-hidden="true">
    <g fill="var(--box-blue)" stroke="var(--box-edge)" stroke-width="1">
      <polygon points="192,176 650,176 668,237 173,237"/>
      <rect x="668" y="237" width="91" height="306"/>
      <path d="M759,242 H780 A26,26 0 0 1 806,268 V517 A26,26 0 0 1 780,543 H759 Z"/>
      <rect x="173" y="543" width="495" height="103"/>
      <polygon points="173,545 157,545 147,554 93,569 93,630 161,636 170,644"/>
      <polygon points="668,545 679,554 734,558 734,619 679,634 670,644"/>
      <rect x="69" y="646" width="104" height="305"/>
      <path d="M69,646 H46 A26,26 0 0 0 20,672 V925 A26,26 0 0 0 46,951 H69 Z"/>
      <rect x="173" y="951" width="495" height="101"/>
      <polygon points="173,953 157,953 147,962 93,977 93,1038 161,1044 170,1052"/>
      <polygon points="668,953 679,962 734,966 734,1027 679,1042 670,1052"/>
    </g>
    <line x1="668" y1="1053" x2="772" y2="1053" stroke="var(--box-edge)" stroke-width="1"/>
  </svg>

  <section class="front front-1">
    <div class="front-glow" role="img" aria-label="Light burst background with botanical leaves"></div>
    <div class="count-badge"><span class="num">24</span><span class="unit">lozenges</span></div>
    <div class="fast-badge"><span class="fast">Fast</span><span class="acting">Acting</span></div>
    <div class="brand-name">TELVAROSE</div>
    <div class="supplement-tag">FOOD SUPPLEMENT</div>
    <div class="claim">for soar throat</div>
    <ul class="benefits">
      <li>- Fast &amp; Effective relief for sore throats</li>
      <li>- Antibacterial Action</li>
      <li>- Helps clear nasal passagers</li>
    </ul>
    <div class="free-icons">
      <div class="free-icon">
        <svg width="30" height="30" viewBox="0 0 30 30"><circle cx="15" cy="15" r="13" fill="none" stroke="var(--lime)" stroke-width="2"/><path d="M13,7 H17 V10 L19,13 V22 H11 V13 L13,10 Z" fill="var(--lime)"/><line x1="7" y1="23" x2="23" y2="7" stroke="var(--lime)" stroke-width="1.8"/></svg>
        LACTOSE<br><b>FREE</b>
      </div>
      <div class="free-icon">
        <svg width="30" height="30" viewBox="0 0 30 30"><circle cx="15" cy="15" r="13" fill="none" stroke="var(--gum-purple)" stroke-width="2"/><text x="15" y="20" text-anchor="middle" font-family="Open Sans, sans-serif" font-weight="700" font-size="13" fill="var(--gum-purple)">30</text></svg>
        <b>CHEWING</b><br><b>GUM</b>
      </div>
      <div class="free-icon">
        <svg width="30" height="30" viewBox="0 0 30 30"><circle cx="15" cy="15" r="13" fill="none" stroke="var(--lime)" stroke-width="2"/><g stroke="var(--lime)" stroke-width="1.6" fill="none"><line x1="15" y1="24" x2="15" y2="8"/><path d="M15,12 l-4,-3 M15,12 l4,-3 M15,16 l-4,-3 M15,16 l4,-3 M15,20 l-4,-3 M15,20 l4,-3"/><line x1="7" y1="23" x2="23" y2="7"/></g></svg>
        GLUTEN<br><b>FREE</b>
      </div>
      <div class="free-icon">
        <svg width="30" height="30" viewBox="0 0 30 30"><circle cx="15" cy="15" r="13" fill="none" stroke="var(--lime)" stroke-width="2"/><polygon points="15,8 21,11 21,18 15,21 9,18 9,11" fill="var(--lime)"/><path d="M9,11 L15,14 L21,11 M15,14 V21" stroke="var(--front-dark)" stroke-width="1" fill="none"/><line x1="7" y1="23" x2="23" y2="7" stroke="var(--lime)" stroke-width="1.8"/></svg>
        SUGAR<br><b>FREE</b>
      </div>
    </div>
  </section>

  <section class="side-panel">
    <div class="varnish-area"><span>RISERVA VERNICE</span></div>
    <div class="batch-info"><p>Lotto:<br>Da consumarsi<br>preferibilmente<br>entro:</p></div>
  </section>

  <section class="side-strip strip-1">
    <div class="supplement-tag">FOOD SUPPLEMENT</div>
    <div class="claim">for soar throat</div>
    <div class="brand-name">TELVAROSE</div>
  </section>

  <section class="front front-2">
    <div class="front-glow" role="img" aria-label="Light burst background with botanical leaves"></div>
    <div class="count-badge"><span class="num">24</span><span class="unit">lozenges</span></div>
    <div class="fast-badge"><span class="fast">Fast</span><span class="acting">Acting</span></div>
    <div class="brand-name">TELVAROSE</div>
    <div class="supplement-tag">FOOD SUPPLEMENT</div>
    <div class="claim">for soar throat</div>
    <ul class="benefits">
      <li>- Fast &amp; Effective relief for sore throats</li>
      <li>- Antibacterial Action</li>
      <li>- Helps clear nasal passagers</li>
    </ul>
    <div class="free-icons">
      <div class="free-icon">
        <svg width="30" height="30" viewBox="0 0 30 30"><circle cx="15" cy="15" r="13" fill="none" stroke="var(--lime)" stroke-width="2"/><path d="M13,7 H17 V10 L19,13 V22 H11 V13 L13,10 Z" fill="var(--lime)"/><line x1="7" y1="23" x2="23" y2="7" stroke="var(--lime)" stroke-width="1.8"/></svg>
        LACTOSE<br><b>FREE</b>
      </div>
      <div class="free-icon">
        <svg width="30" height="30" viewBox="0 0 30 30"><circle cx="15" cy="15" r="13" fill="none" stroke="var(--gum-purple)" stroke-width="2"/><text x="15" y="20" text-anchor="middle" font-family="Open Sans, sans-serif" font-weight="700" font-size="13" fill="var(--gum-purple)">30</text></svg>
        <b>CHEWING</b><br><b>GUM</b>
      </div>
      <div class="free-icon">
        <svg width="30" height="30" viewBox="0 0 30 30"><circle cx="15" cy="15" r="13" fill="none" stroke="var(--lime)" stroke-width="2"/><g stroke="var(--lime)" stroke-width="1.6" fill="none"><line x1="15" y1="24" x2="15" y2="8"/><path d="M15,12 l-4,-3 M15,12 l4,-3 M15,16 l-4,-3 M15,16 l4,-3 M15,20 l-4,-3 M15,20 l4,-3"/><line x1="7" y1="23" x2="23" y2="7"/></g></svg>
        GLUTEN<br><b>FREE</b>
      </div>
      <div class="free-icon">
        <svg width="30" height="30" viewBox="0 0 30 30"><circle cx="15" cy="15" r="13" fill="none" stroke="var(--lime)" stroke-width="2"/><polygon points="15,8 21,11 21,18 15,21 9,18 9,11" fill="var(--lime)"/><path d="M9,11 L15,14 L21,11 M15,14 V21" stroke="var(--front-dark)" stroke-width="1" fill="none"/><line x1="7" y1="23" x2="23" y2="7" stroke="var(--lime)" stroke-width="1.8"/></svg>
        SUGAR<br><b>FREE</b>
      </div>
    </div>
  </section>

  <section class="side-strip strip-2">
    <div class="supplement-tag">FOOD SUPPLEMENT</div>
    <div class="claim">for soar throat</div>
    <div class="brand-name">TELVAROSE</div>
  </section>
</div>
</body>
</html>
```